Business Card For Birchfield Property Partners Corp.
Birchfield Property Partners Corp.
Business Card For Birchfield Property Partners Corp. - Real Estate
Creative Brief
Modern
Warren T. Caldwell
Owner
418 Larkspur Avenue, Huntington NY 11749
warrencaldwell@brightmailer.net
www.birchfieldpropertypartners.com
Catch Phrases: Complete Home Service Solution Take your first step toward financial freedom today
Maybe Some other design symbolizing fast cash for homes with a catch phrase: Birchfield Property Partners will purchase any home in any condition

```html
<!DOCTYPE html>
<html lang="en">
<head>
<meta charset="utf-8">
<title>Birchfield Property Partners Corp. – Stationery</title>
<link href="https://fonts.googleapis.com/css2?family=Open+Sans:wght@400;600;700;800&display=swap" rel="stylesheet">
<style>
  :root{
    --bg:#eef0f2;
    --paper:#ffffff;
    --brand-blue:#2a5d8f;
    --band-dark:#1f4f80;
    --band-light:#4f8cc0;
    --accent-green:#7ab648;
    --ink:#4a5561;
    --ink-soft:#8a96a3;
    --shadow:0 2px 8px rgba(0,0,0,.12);
  }
  *{box-sizing:border-box;margin:0;padding:0}
  html,body{width:1200px;height:936px;overflow:hidden}
  body{background:var(--bg);font-family:"Open Sans",Arial,sans-serif;position:relative;color:var(--ink)}
  .sheet{position:absolute;background:var(--paper);box-shadow:var(--shadow);overflow:hidden}
  .brand{color:var(--brand-blue);font-weight:800;letter-spacing:.2px;line-height:1.05;display:flex;align-items:center;gap:.4em}
  .brand-dot{width:.7em;height:.7em;background:var(--accent-green);flex:none}
  .band{position:absolute;left:0;right:0;background:linear-gradient(90deg,var(--band-dark),var(--band-light) 50%,var(--band-dark));color:#fff;text-align:center;font-weight:600;letter-spacing:1.5px;display:flex;align-items:center;justify-content:center}
  .band::before{content:"";position:absolute;left:0;right:0;top:-3px;height:2px;background:var(--accent-green)}
  .contact{position:absolute;font-size:7px;line-height:1.7;color:var(--ink);white-space:nowrap}
  .contact li{list-style:none;display:flex;align-items:center;gap:4px}
  .contact li::before{content:"";width:5px;height:5px;background:var(--brand-blue);flex:none}

  /* letterhead */
  .letterhead{left:183px;top:63px;width:388px;height:538px}
  .letterhead .brand{position:absolute;left:26px;top:30px;font-size:15px;width:170px}
  .letterhead .contact{right:18px;top:26px;font-size:6px;line-height:1.75}
  .letterhead .contact li::before{width:4px;height:4px}
  .letterhead .watermark{position:absolute;left:0;right:0;top:250px;text-align:center;font-size:30px;font-weight:800;color:var(--brand-blue);opacity:.07;line-height:1.1}
  .letterhead .band{bottom:22px;height:24px;font-size:8px}

  /* folder */
  .folder{left:634px;top:51px;width:462px;height:550px}
  .folder .brand{position:absolute;left:0;right:0;top:250px;justify-content:center;flex-direction:column;text-align:center;font-size:34px;gap:14px}
  .folder .brand-dot{width:26px;height:26px}
  .folder .band{bottom:22px;height:26px;font-size:8px}

  /* business cards */
  .card-front{left:76px;top:652px;width:165px;height:109px}
  .card-front .brand{position:absolute;left:9px;top:12px;font-size:8px;width:80px}
  .card-front .contact{left:96px;top:8px;font-size:3.6px;line-height:1.9}
  .card-front .contact li::before{width:3px;height:3px}
  .card-front .person{position:absolute;left:9px;top:48px;font-size:5px;line-height:1.5}
  .card-front .person b{color:var(--brand-blue);font-size:6px}
  .card-front .band{bottom:6px;height:11px;font-size:4.5px;letter-spacing:.5px}
  .card-back{left:76px;top:781px;width:165px;height:107px;background:linear-gradient(160deg,var(--band-light),var(--band-dark));display:flex;flex-direction:column;align-items:center;justify-content:center;gap:10px}
  .card-back .brand{color:#fff;font-size:9px}
  .card-back .web{color:#dce8f3;font-size:4.5px;letter-spacing:.8px}

  /* envelope front */
  .envelope-front{left:264px;top:654px;width:434px;height:234px}
  .envelope-front .brand{position:absolute;left:24px;top:22px;font-size:15px;width:200px}
  .envelope-front .address{position:absolute;left:24px;top:68px;font-size:6.5px;color:var(--ink)}
  .envelope-front .band{bottom:34px;height:24px;font-size:8px}

  /* envelope back */
  .envelope-back{left:736px;top:654px;width:418px;height:234px}
  .envelope-back svg{position:absolute;left:0;top:0}
  .envelope-back .web{position:absolute;left:0;right:0;top:30px;text-align:center;color:#fff;font-size:10px;font-weight:600;letter-spacing:2px}
</style>
</head>
<body>

<section class="sheet letterhead">
  <div class="brand"><span class="brand-dot"></span>Birchfield Property Partners</div>
  <ul class="contact">
    <li>418 Larkspur Avenue, Huntington</li>
    <li>(631) 555-0148</li>
    <li>(631) 555-0149</li>
    <li>(631) 555-0150</li>
    <li>warrencaldwell@brightmailer.net</li>
  </ul>
  <div class="watermark" aria-hidden="true">Birchfield<br>Property Partners</div>
  <div class="band">www.birchfieldpropertypartners.com</div>
</section>

<section class="sheet folder">
  <div class="brand"><span class="brand-dot"></span><span>Birchfield<br>Property Partners</span></div>
  <div class="band">www.birchfieldpropertypartners.com</div>
</section>

<section class="sheet card-front">
  <div class="brand"><span class="brand-dot"></span>Birchfield Property Partners</div>
  <ul class="contact">
    <li>(631) 555-0148</li>
    <li>(631) 555-0149</li>
    <li>418 Larkspur Ave</li>
    <li>warrencaldwell@brightmailer.net</li>
  </ul>
  <div class="person"><b>Warren T. Caldwell</b><br>Owner</div>
  <div class="band">www.birchfieldpropertypartners.com</div>
</section>

<section class="sheet card-back">
  <div class="brand">Birchfield Property Partners</div>
  <div class="web">www.birchfieldpropertypartners.com</div>
</section>

<section class="sheet envelope-front">
  <div class="brand"><span class="brand-dot"></span>Birchfield Property Partners</div>
  <div class="address">418 Larkspur Avenue, Huntington NY 11749</div>
  <div class="band">www.birchfieldpropertypartners.com</div>
</section>

<section class="sheet envelope-back">
  <svg width="418" height="234" viewBox="0 0 418 234" aria-hidden="true">
    <defs>
      <linearGradient id="flap" x1="0" y1="0" x2="1" y2="0">
        <stop offset="0" stop-color="#1f4f80"/>
        <stop offset=".5" stop-color="#4f8cc0"/>
        <stop offset="1" stop-color="#1f4f80"/>
      </linearGradient>
    </defs>
    <path d="M0 0 H418 V62 Q418 70 400 74 L220 104 Q209 106 198 104 L18 74 Q0 70 0 62 Z" fill="url(#flap)"/>
  </svg>
  <div class="web">www.birchfieldpropertypartners.com</div>
</section>

</body>
</html>
```